Golden Coat All-Purpose Breading Bag Design

Our client, Harlow Food Products, is looking to re-design the packaging for their product, Pellworth's Golden Coat. Goldn Coat is an all-purpose food breading mix.

Harlow Foods has a registered trademark for this product, but they have not been using it for this particular 10 pound bag. They want to get the trademark onto the bag and also give the bag an updated look. They would like to continue to use the same red and blue colors. This 10 pound bag is not available on store shelves; it is sold to food service distributors who sell to restaurants.

All of the copy on the existing bag is still relevant, so we will want to incoprporate it into the bag design. Once these bags are filled with product, the tops get folded over about 1 inch and then sewn shut with thread.

Eventually, we will need the design applied to the Bag Template file attached, but that isn't important until a design is selected.

Target Market(s)

Restaurants

Industry/Entity Type

Food Manufacturing

Colors
0054AA
0677BA
7BADD7
CADEEF
E8F1F8
EB3D1F
EC4F4E
F09395
F8D3D4
FCEDEE

Requirements
Must have
• Trademark introduced to the design

```html
<!DOCTYPE html>
<html lang="en">
<head>
<meta charset="utf-8">
<title>Pellworth's Golden Coat – Bag Layout</title>
<link href="https://fonts.googleapis.com/css2?family=Montserrat:wght@400;500;600;700;800&display=swap" rel="stylesheet">
<style>
  :root {
    --stage: #4d4d4d;
    --paper: #e6e6e6;
    --red: #ec4f4e;
    --blue: #1453a8;
    --yellow: #f5e61b;
    --ink: #222222;
    --white: #ffffff;
    --soft-grey: #e8e8e8;
  }
  * { box-sizing: border-box; margin: 0; padding: 0; }
  html, body { width: 1200px; height: 900px; overflow: hidden; }
  body { background: var(--stage); font-family: 'Montserrat', sans-serif; position: relative; }

  .bag { position: absolute; left: 65px; top: 73px; width: 1068px; height: 597px; background: var(--paper); }
  .bag-flap { position: absolute; left: 296px; top: 670px; width: 266px; height: 162px; background: var(--paper); }

  .fold { position: absolute; top: 0; height: 100%; }
  .fold-a { left: 215px; width: 60px; background: linear-gradient(90deg, rgba(0,0,0,0.06), rgba(0,0,0,0)); }
  .fold-b { left: 412px; width: 130px; background: linear-gradient(90deg, rgba(0,0,0,0), rgba(0,0,0,0.05)); }
  .fold-c { left: 542px; width: 50px; background: linear-gradient(90deg, rgba(0,0,0,0.07), rgba(0,0,0,0.02)); }
  .fold-d { left: 700px; width: 43px; background: linear-gradient(90deg, rgba(0,0,0,0.02), rgba(0,0,0,0.06)); }

  .wordmark { position: absolute; text-align: center; color: var(--blue); font-weight: 800; }
  .wordmark .maker, .wordmark .name { display: block; }
  .wordmark-side .maker { font-size: 18px; line-height: 1.2; margin-bottom: 4px; }
  .wordmark-side .name { font-size: 36px; line-height: 1.1; }
  .wordmark-front .maker { font-size: 34px; line-height: 1.2; margin-bottom: 6px; }
  .wordmark-front .name { font-size: 66px; line-height: 1.1; }
  .wm-left { left: 65px; top: 200px; width: 215px; }
  .wm-front { left: 280px; top: 150px; width: 327px; }
  .wm-right { left: 607px; top: 200px; width: 198px; }
  .wm-back { left: 806px; top: 150px; width: 327px; }

  .red-box { position: absolute; background: var(--red); border: 2px solid var(--ink); color: var(--white); }

  .about { left: 97px; top: 391px; width: 156px; height: 246px; padding: 11px 7px; font-size: 9px; line-height: 1.32; text-align: center; font-weight: 500; overflow: hidden; }
  .about p + p { margin-top: 9px; }

  .breading { position: absolute; left: 285px; top: 419px; width: 302px; height: 219px; border: 2px solid var(--ink); background: var(--soft-grey); }
  .breading-head { position: absolute; left: 0; top: 0; width: 210px; height: 96px; background: var(--red); color: var(--white); text-align: center; border-right: 2px solid var(--ink); border-bottom: 2px solid var(--ink); }
  .breading-head .kicker { font-size: 15px; font-weight: 500; letter-spacing: 1.5px; margin-top: 14px; }
  .breading-head .title { font-size: 32px; font-weight: 800; line-height: 1.0; margin-top: 2px; }
  .breading-head .tagline { font-size: 8px; font-weight: 600; letter-spacing: 1px; margin-top: 4px; }
  .breading-slogan { position: absolute; left: 210px; top: 0; width: 88px; height: 96px; background: var(--red); color: var(--white); font-size: 10px; font-weight: 700; line-height: 1.3; text-align: center; padding-top: 12px; border-bottom: 2px solid var(--ink); }
  .accent { color: var(--yellow); }
  .ingredients { position: absolute; left: 0; top: 96px; width: 100%; height: 86px; text-align: center; }
  .section-label { color: var(--blue); font-weight: 700; letter-spacing: 1.5px; font-size: 12px; }
  .ingredients .section-label { margin-top: 12px; }
  .rule { height: 2px; background: var(--blue); margin: 5px auto 0; }
  .ingredients .rule { width: 272px; }
  .ingredients p { font-size: 10px; line-height: 1.45; color: var(--ink); margin-top: 8px; padding: 0 10px; }
  .breading-foot { position: absolute; left: 0; bottom: 0; width: 100%; height: 35px; background: var(--blue); border-top: 2px solid var(--ink); color: var(--white); }
  .breading-foot .claim { position: absolute; left: 8px; top: 7px; width: 110px; font-size: 6.5px; line-height: 1.35; text-align: center; }
  .breading-foot .maker-info { position: absolute; left: 188px; top: 5px; font-size: 6.5px; line-height: 1.35; }
  .breading-foot .maker-info strong { font-weight: 700; }
  .weight-badge { position: absolute; left: 122px; top: -20px; width: 50px; height: 50px; border-radius: 50%; background: #1e1e1e; color: var(--white); text-align: center; padding-top: 11px; font-size: 8px; line-height: 1.2; }
  .weight-badge b { display: block; font-size: 13px; font-weight: 500; }

  .directions { position: absolute; left: 622px; top: 431px; width: 156px; height: 206px; border: 2px solid var(--ink); background: var(--white); }
  .directions-head { height: 61px; text-align: center; border-bottom: 2px solid var(--ink); background: var(--soft-grey); }
  .directions-head .kicker { font-size: 9px; font-weight: 600; letter-spacing: 1px; padding-top: 14px; color: var(--ink); }
  .directions-head .section-label { font-size: 16px; letter-spacing: 2.5px; margin-top: 3px; }
  .directions-steps { background: var(--red); color: var(--white); height: 98px; border-bottom: 2px solid var(--ink); padding: 12px 10px 0 14px; font-size: 9px; line-height: 1.3; list-style: none; }
  .directions-steps li { position: relative; padding-left: 12px; margin-bottom: 5px; }
  .directions-steps li::before { content: ""; position: absolute; left: 0; top: 4px; width: 5px; height: 5px; border-radius: 50%; background: var(--white); }
  .directions-tip { font-size: 9.5px; line-height: 1.35; text-align: center; color: var(--ink); padding: 9px 6px 0; background: var(--soft-grey); height: 43px; }

  .frying { position: absolute; left: 820px; top: 447px; width: 289px; height: 188px; border: 2px solid var(--ink); background: var(--soft-grey); }
  .frying-head { height: 118px; background: var(--red); color: var(--white); text-align: center; border-bottom: 2px solid var(--ink); }
  .frying-head .small { font-size: 15px; font-weight: 500; letter-spacing: 1px; padding-top: 8px; line-height: 1; }
  .frying-head .big { font-size: 27px; font-weight: 800; line-height: 1.05; }
  .frying-head .and { font-size: 15px; font-weight: 500; line-height: 1; }
  .frying-head .note { font-size: 8px; letter-spacing: 0.8px; margin-top: 2px; }
  .frying-uses { text-align: center; }
  .frying-uses .section-label { margin-top: 6px; }
  .frying-uses .rule { width: 262px; }
  .frying-uses p { font-size: 10px; line-height: 1.45; color: var(--ink); margin-top: 8px; }

  .flap-slogan { position: absolute; left: 314px; top: 687px; width: 248px; height: 125px; background: var(--blue); border: 2px solid var(--ink); color: var(--white); text-align: center; font-size: 12.5px; font-weight: 700; line-height: 1.35; padding-top: 29px; letter-spacing: 0.3px; }
</style>
</head>
<body>
  <div class="bag">
    <div class="fold fold-a"></div>
    <div class="fold fold-b"></div>
    <div class="fold fold-c"></div>
    <div class="fold fold-d"></div>
  </div>
  <div class="bag-flap"></div>

  <!-- Side gusset, left -->
  <div class="wordmark wordmark-side wm-left"><span class="maker">Pellworth's</span><span class="name">Golden<br>Coat</span></div>
  <div class="red-box about">
    <p>Pellworth's Golden Coat is a prepared formula of pure foods that enables you to fry chicken from the raw to the well done in ten minutes. It seals in all the natural juice and creates a very thin crunchy coating which the fat does not penetrate- thereby using much less fat than ordinary frying methods.</p>
    <p>This formula is an all-dry mix to be used on anything breaded- fish, oysters, shrimp, veal and chicken fried steak.</p>
  </div>

  <!-- Front panel -->
  <div class="wordmark wordmark-front wm-front"><span class="maker">Pellworth's</span><span class="name">Golden<br>Coat</span></div>
  <div class="breading">
    <div class="breading-head">
      <div class="kicker">THE ALL PURPOSE</div>
      <div class="title">BREADING</div>
      <div class="tagline">SEALS JUICE IN- GREASE OUT</div>
    </div>
    <div class="breading-slogan">FOOD FRIED<br><span class="accent">THE GOLDEN<br>COAT WAY IS</span><br>FRIED FOOD<br><span class="accent">THE RIGHT WAY</span></div>
    <div class="ingredients">
      <div class="section-label">INGREDIENTS</div>
      <div class="rule"></div>
      <p>flour, salt, non-fat milk solids, egg yolk, baking powder, corn starch, sugar and pepper</p>
    </div>
    <div class="breading-foot">
      <div class="claim">Cooks two-pound chicken well done in 10 minutes(deep fat)</div>
      <div class="weight-badge">Net Wt.<b>10 Lbs</b></div>
      <div class="maker-info">by <strong>Harlow Food Products</strong><br>742 Maple Court<br>Fairview, Kansas 66012</div>
    </div>
  </div>

  <!-- Side gusset, right -->
  <div class="wordmark wordmark-side wm-right"><span class="maker">Pellworth's</span><span class="name">Golden<br>Coat</span></div>
  <div class="directions">
    <div class="directions-head">
      <div class="kicker">NOTHING TO ADD</div>
      <div class="section-label">DIRECTIONS</div>
    </div>
    <ul class="directions-steps">
      <li>Wet all foods in water</li>
      <li>Place in dry dip, coating thoroughly</li>
      <li>Deep fry at 350°F for 10 minutes</li>
    </ul>
    <div class="directions-tip">For best results double dip onion rings and oysters</div>
  </div>

  <!-- Back panel -->
  <div class="wordmark wordmark-front wm-back"><span class="maker">Pellworth's</span><span class="name">Golden<br>Coat</span></div>
  <div class="frying">
    <div class="frying-head">
      <div class="small">FOR</div>
      <div class="big">DEEP FAT</div>
      <div class="and">AND</div>
      <div class="big">PAN FRYING</div>
      <div class="note">(slightly longer on pan frying)</div>
    </div>
    <div class="frying-uses">
      <div class="section-label">CAN BE USED FOR</div>
      <div class="rule"></div>
      <p>chicken, steaks, chops, tenderloin. fish, shrimp,<br>oyster and other sea foods, onion rings and vegetables</p>
    </div>
  </div>

  <!-- Bottom flap -->
  <div class="flap-slogan">CHICKEN FRIED<br><span class="accent">THE GOLDEN COAT WAY</span><br>IS THE FRIED CHICKEN<br><span class="accent">THE RIGHT WAY</span></div>
</body>
</html>
```